Bref créative |
Birch Hydraulic | ||
Use same font as used in my logo | ||
Cutting-Edge Corporate Professional Simple |
Paul Destry | ||
Owner | ||
4637 Heron Ridge Lane Clarkston MI 48351 |
destry.paul@mailvane.net | ||

```html
<!DOCTYPE html>
<html lang="en">
<head>
<meta charset="utf-8">
<title>Birch Hydraulic Stationery</title>
<link href="https://fonts.googleapis.com/css2?family=Roboto+Condensed:wght@400;700&display=swap" rel="stylesheet">
<style>
  :root{
    --stage:#000000;
    --paper:#ffffff;
    --green-dark:#0d5a2a;
    --green-mid:#1f8a3b;
    --green-light:#8fd14f;
    --lime:#a6e05a;
    --ink:#333333;
  }
  *{margin:0;padding:0;box-sizing:border-box}
  html,body{width:1200px;height:1047px;overflow:hidden;background:var(--stage)}
  body{position:relative;font-family:"Roboto Condensed",Arial,sans-serif;color:var(--ink)}
  .wordmark{font-family:"Roboto Condensed",Arial,sans-serif;font-weight:700;color:var(--green-dark);text-transform:uppercase;line-height:1;text-align:center;letter-spacing:.5px}

  /* Letterhead */
  .letterhead{position:absolute;left:475px;top:57px;width:516px;height:939px;background:var(--paper)}
  .letterhead .header-band{position:absolute;left:0;top:0;width:516px;height:130px}
  .letterhead .wordmark{position:absolute;left:0;right:0;top:48px;font-size:22px}
  .letterhead .footer-band{position:absolute;left:0;bottom:0;width:100%;height:48px;background:var(--green-dark);color:#fff;font-size:9.5px;text-align:center;padding-top:11px;line-height:1.6}

  /* Business card */
  .business-card{position:absolute;left:204px;top:161px;width:116px;height:292px;background:linear-gradient(180deg,#1a7a34 0%,var(--green-dark) 70%);overflow:hidden}
  .business-card .wordmark{color:#fff;font-size:13px;margin-top:34px}
  .business-card .holder{margin-top:58px;text-align:center;color:#fff}
  .business-card .holder-name{font-size:10px;font-weight:700;text-transform:uppercase}
  .business-card .holder-role{font-size:8px}
  .business-card .contact{margin:20px 0 0 14px;font-size:7px;line-height:1.45;color:var(--lime)}
  .business-card .card-foot{position:absolute;left:0;bottom:0;width:116px;height:70px}
  .business-card .card-email{position:absolute;left:0;right:0;bottom:18px;text-align:center;font-size:7.5px;color:var(--green-dark);font-weight:700}

  /* Envelope */
  .envelope{position:absolute;left:57px;top:515px;width:764px;height:328px;background:var(--paper);border-top:6px solid var(--green-dark);overflow:hidden}
  .envelope .wordmark{position:absolute;left:0;right:0;top:38px;font-size:24px}
  .envelope .return-address{position:absolute;left:38px;top:144px;font-size:10.5px;line-height:1.45;color:var(--ink)}
  .envelope .window{position:absolute;left:452px;top:168px;width:261px;height:104px;background:#e9e9e9;border:1px solid #d0d0d0;border-radius:4px}
  .envelope .swoosh{position:absolute;left:0;bottom:0;width:764px;height:40px}
</style>
</head>
<body>

<section class="letterhead">
  <svg class="header-band" viewBox="0 0 516 130" aria-hidden="true">
    <defs>
      <radialGradient id="lh-grad" cx="50%" cy="30%" r="65%">
        <stop offset="0" stop-color="#e8f7e4"/>
        <stop offset=".55" stop-color="#6cc070"/>
        <stop offset="1" stop-color="#0d5a2a"/>
      </radialGradient>
    </defs>
    <path d="M0 0H516V118Q258 28 0 118Z" fill="url(#lh-grad)"/>
    <path d="M0 118Q258 28 516 118" fill="none" stroke="#0d5a2a" stroke-width="3"/>
  </svg>
  <div class="wordmark">Birch Hydraulic</div>
  <footer class="footer-band">
    4637 Heron Ridge Lane, Clarkston MI 48351<br>
    P: 586-402-1180 &nbsp;|&nbsp; C: 586-519-3364 &nbsp;|&nbsp; F: 586-402-1183 &nbsp;|&nbsp; E: destry.paul@mailvane.net
  </footer>
</section>

<section class="business-card">
  <div class="wordmark">Birch<br>Hydraulic</div>
  <div class="holder">
    <div class="holder-name">Paul Destry</div>
    <div class="holder-role">Owner</div>
  </div>
  <div class="contact">
    4637 Heron Ridge Lane<br>Clarkston MI 48351<br><br>
    P: 586-402-1180<br>C: 586-519-3364<br>F: 586-402-1183
  </div>
  <svg class="card-foot" viewBox="0 0 116 70" aria-hidden="true">
    <path d="M0 14Q58 -4 116 14V70H0Z" fill="#ffffff"/>
    <path d="M0 14Q58 -4 116 14" fill="none" stroke="#8fd14f" stroke-width="2"/>
  </svg>
  <div class="card-email">destry.paul@mailvane.net</div>
</section>

<section class="envelope">
  <div class="wordmark">Birch<br>Hydraulic</div>
  <address class="return-address" style="font-style:normal">
    4637 Heron Ridge Lane<br>Clarkston MI 48351<br>
    P: 586-402-1180<br>C: 586-519-3364<br>F: 586-402-1183<br>E: destry.paul@mailvane.net
  </address>
  <div class="window"></div>
  <svg class="swoosh" viewBox="0 0 764 40" preserveAspectRatio="none" aria-hidden="true">
    <defs>
      <linearGradient id="env-grad" x1="0" x2="1">
        <stop offset="0" stop-color="#1f8a3b"/>
        <stop offset=".35" stop-color="#8fd14f"/>
        <stop offset=".6" stop-color="#ffffff" stop-opacity="0"/>
      </linearGradient>
    </defs>
    <path d="M0 40V18Q250 8 520 30L540 40Z" fill="url(#env-grad)"/>
  </svg>
</section>

</body>
</html>
```